WEBSITE NEEDED FOR MY COMPANY CALLED BRAVERIDGE HOCKEY DEVELOPMENT

LOOKING FOR A WEBSITE TO MARKET AND SEEL MY HOCKEY DEVELOPMENT PROGRAMS.
NEEDS TO HAVE 5+ PAGES

Target Market(s)

YOUTH SPORTS

Industry/Entity Type

YOUTH ATHLETE DEVELOPMENT

Number of Pages Required

5+ page

Font styles to use
Sans Serif

Colors
0054AA
0677BA
7BADD7
CADEEF
E8F1F8

Requirements
Must have
• MAIN PAGE - SPIRNG PROGRAM PAGE - SUMMER PROGRAM PAGE - WINTER PAGE - TOURNAMENT PAGE
Nice to have
• FLASH
Should not have
• NOT SURE

```html
<!DOCTYPE html>
<html lang="en">
<head>
<meta charset="utf-8">
<title>Spring Program – Braveridge Hockey Development</title>
<link href="https://fonts.googleapis.com/css2?family=Roboto+Condensed:wght@400;700&family=Roboto:wght@300;400;500&family=Open+Sans:wght@400;700&display=swap" rel="stylesheet">
<style>
:root{
  --blue:#0677ba;
  --deep-blue:#0054aa;
  --sky:#7badd7;
  --ice:#cadeef;
  --frost:#e8f1f8;
  --navy:#1f3042;
  --footer:#243447;
  --footer-bottom:#1b2735;
  --ink:#222;
  --muted:#777;
  --card:#f6f6f6;
  --white:#fff;
}
*{margin:0;padding:0;box-sizing:border-box}
html,body{width:1200px;height:2498px;overflow:hidden;background:var(--white)}
body{position:relative;font-family:'Roboto',sans-serif;color:var(--ink)}

.site-header{position:absolute;top:0;left:0;width:1200px;height:78px;background:var(--white);z-index:2}
.brand{position:absolute;left:0;top:0;width:270px;height:93px;background:var(--navy);clip-path:polygon(0 0,100% 0,85% 100%,0 100%);display:flex;flex-direction:column;justify-content:center;padding-left:38px}
.brand-name{font-family:'Roboto Condensed',sans-serif;font-weight:700;font-size:19px;line-height:22px;color:#2fb4e6;letter-spacing:.5px}
.main-nav{position:absolute;left:411px;top:34px;display:flex;gap:0}
.main-nav a{position:absolute;white-space:nowrap;font-size:11.5px;color:#333;text-decoration:none;font-weight:400}
.main-nav a.active{color:var(--blue)}
.header-social{position:absolute;top:35px;left:922px;display:flex;gap:19px}
.header-social span{width:12px;height:12px;border-radius:50%;border:1.5px solid #444}
.contact-btn{position:absolute;left:1032px;top:20px;width:130px;height:37px;border:2px solid var(--deep-blue);color:var(--deep-blue);font-size:11px;font-weight:500;display:flex;align-items:center;justify-content:center}

.hero{position:absolute;top:78px;left:0;width:1200px;height:392px;background:radial-gradient(circle at 72% 55%,#9fc4ef 0%,#3b5c9a 14%,#14203f 40%,#0a1226 75%),#0a1226}
.hero-photo{position:absolute;inset:0}
.hero-title{position:absolute;left:125px;top:128px;font-family:'Roboto Condensed',sans-serif;font-weight:700;font-size:56px;color:var(--white)}
.hero-text{position:absolute;left:125px;top:202px;width:400px;font-size:14px;line-height:25px;color:var(--white)}

.info-band{position:absolute;top:0;left:0;width:1200px;height:533px}
.info-band svg{position:absolute;top:0;left:0}
.band-left{position:absolute;left:482px;top:430px;font-family:'Roboto Condensed',sans-serif;color:var(--white)}
.band-left strong{display:block;font-size:32px;line-height:36px}
.band-left span{display:block;font-size:27px;line-height:36px;font-weight:400}
.band-right{position:absolute;left:839px;top:432px;font-family:'Roboto Condensed',sans-serif;font-weight:700;color:var(--white);font-size:25px;line-height:37px}
.band-right u{text-underline-offset:5px}
.band-icon{position:absolute;left:773px;top:440px}

.intro{position:absolute;top:588px;left:0;width:1200px;text-align:center;font-size:25px;line-height:40px;color:#333;font-weight:400}

.programs{position:absolute;left:125px;top:719px;display:grid;grid-template-columns:repeat(3,286px);column-gap:46px;row-gap:43px}
.program-card{position:relative;width:286px;height:407px;background:var(--card)}
.program-photo{height:199px;background:linear-gradient(160deg,#eceef2 0%,#d7dbe2 55%,#e6c8b5 100%)}
.day-tag{position:absolute;top:0;right:0;width:120px;height:37px;background:var(--deep-blue);clip-path:polygon(20% 0,100% 0,100% 100%,0 100%);color:var(--white);font-size:12px;font-weight:500;display:flex;align-items:center;justify-content:center;padding-left:14px}
.card-head{position:absolute;left:19px;right:23px;top:220px;display:flex;justify-content:space-between;font-family:'Roboto Condensed',sans-serif;font-weight:700;font-size:17px}
.card-head .price{color:var(--blue)}
.card-text{position:absolute;left:19px;top:252px;width:250px;font-size:12.5px;line-height:23.5px;color:var(--muted);font-weight:300}
.card-dates{position:absolute;left:19px;top:339px;font-size:11.5px;line-height:23.5px;color:#444}
.card-dates b{color:#222;font-weight:500}
.more{position:absolute;right:23px;top:362px;font-size:12px;line-height:23.5px;color:var(--deep-blue);font-weight:500}

.site-footer{position:absolute;top:2133px;left:0;width:1200px;height:316px;background:var(--footer);color:var(--white);font-family:'Open Sans',sans-serif}
.footer-contact{position:absolute;right:716px;top:93px;text-align:right}
.footer-contact h3,.footer-about h3{font-family:'Roboto Condensed',sans-serif;font-size:16px;font-weight:700;margin-bottom:10px}
.contact-line{display:flex;justify-content:flex-end;align-items:center;gap:12px;font-size:11.5px;line-height:24px}
.contact-line svg{width:10px;height:10px}
.footer-badge{position:absolute;left:541px;top:61px;width:120px;height:120px;border:3px solid #2fb4e6;border-radius:50%;display:flex;align-items:center;justify-content:center;text-align:center;font-family:'Roboto Condensed',sans-serif;font-weight:700;font-size:12px;line-height:15px;color:#2fb4e6}
.footer-about{position:absolute;left:716px;top:93px;width:220px}
.footer-about p{font-size:11.5px;line-height:19px}
.footer-social{position:absolute;left:520px;top:231px;display:flex;gap:16px}
.footer-social span{width:28px;height:28px;border-radius:50%;border:1px solid rgba(255,255,255,.7)}
.footer-bottom{position:absolute;top:2449px;left:0;width:1200px;height:49px;background:var(--footer-bottom);color:var(--white);font-size:11.5px;display:flex;align-items:center;justify-content:center;font-family:'Open Sans',sans-serif}
</style>
</head>
<body>

<header class="site-header">
  <div class="brand"><span class="brand-name">BRAVERIDGE<br>HOCKEY DEVELOPMENT</span></div>
  <nav class="main-nav">
    <a style="left:0">HOME</a>
    <a class="active" style="left:67px">OUR PROGRAM</a>
    <a style="left:182px">TOURNAMENT</a>
    <a style="left:291px">NEWS &amp; EVENTS</a>
    <a style="left:412px">ABOUT US</a>
  </nav>
  <div class="header-social"><span></span><span></span><span></span></div>
  <div class="contact-btn">CONTACT US</div>
</header>

<section class="hero">
  <div class="hero-photo" role="img" aria-label="Two hockey players battling on the ice under bright arena spotlights"></div>
  <h1 class="hero-title">Spring Program</h1>
  <p class="hero-text">Lorem ipsum dolor sit amet, consectetur adipiscing eiusmod tempor incididunt ut labore et dolore magna aliqua.</p>
</section>

<div class="info-band">
  <svg width="1200" height="533"><polygon points="446,407 1200,407 1200,533 361,533" fill="var(--blue)"/></svg>
  <div class="band-left"><strong>App - June</strong><span>Include 10 Programs</span></div>
  <svg class="band-icon" width="52" height="60" viewBox="0 0 52 60" fill="none" stroke="#fff" stroke-width="2">
    <path d="M44 2 L24 50 L6 52 Q2 52 3 48 L22 46"/>
    <ellipse cx="38" cy="52" rx="6" ry="3"/>
  </svg>
  <div class="band-right">For More Details About Program<br>Call Now &nbsp;<u>+12 345 67890</u></div>
</div>

<p class="intro">Registration is now open for Spring 2022 Skill Development<br>classes at Braveridge Hockey Development</p>

<main class="programs">
  <article class="program-card"><div class="program-photo" role="img" aria-label="Players in orange jerseys at a faceoff"></div><span class="day-tag">MONDAY</span><div class="card-head"><span>Class Name Here</span><span class="price">$300.00</span></div><p class="card-text">Lorem ipsum dolor sit amet, consectetur adipiscing elit, sed do eiusmod tempor incididunt ut labore et dolore magna...</p><p class="card-dates"><b>Start date:</b> 22-05-2022<br><b>End date:</b> 22-08-2022</p><span class="more">MORE DETAIL</span></article>
  <article class="program-card"><div class="program-photo" role="img" aria-label="Young player in a helmet on the bench"></div><span class="day-tag">TUESDAY</span><div class="card-head"><span>Class Name Here</span><span class="price">$400.00</span></div><p class="card-text">Lorem ipsum dolor sit amet, consectetur adipiscing elit, sed do eiusmod tempor incididunt ut labore et dolore magna...</p><p class="card-dates"><b>Start date:</b> 22-05-2022<br><b>End date:</b> 22-08-2022</p><span class="more">MORE DETAIL</span></article>
  <article class="program-card"><div class="program-photo" role="img" aria-label="Faceoff with referee on the ice"></div><span class="day-tag">FRIDAY</span><div class="card-head"><span>Class Name Here</span><span class="price">$200.00</span></div><p class="card-text">Lorem ipsum dolor sit amet, consectetur adipiscing elit, sed do eiusmod tempor incididunt ut labore et dolore magna...</p><p class="card-dates"><b>Start date:</b> 22-05-2022<br><b>End date:</b> 22-08-2022</p><span class="more">MORE DETAIL</span></article>
  <article class="program-card"><div class="program-photo" role="img" aria-label="Player in a white jersey skating"></div><span class="day-tag">SATURDAY</span><div class="card-head"><span>Class Name Here</span><span class="price">$100.00</span></div><p class="card-text">Lorem ipsum dolor sit amet, consectetur adipiscing elit, sed do eiusmod tempor incididunt ut labore et dolore magna...</p><p class="card-dates"><b>Start date:</b> 22-05-2022<br><b>End date:</b> 22-08-2022</p><span class="more">MORE DETAIL</span></article>
  <article class="program-card"><div class="program-photo" role="img" aria-label="Player skating with the puck"></div><span class="day-tag">SUNDAY</span><div class="card-head"><span>Class Name Here</span><span class="price">$300.00</span></div><p class="card-text">Lorem ipsum dolor sit amet, consectetur adipiscing elit, sed do eiusmod tempor incididunt ut labore et dolore magna...</p><p class="card-dates"><b>Start date:</b> 22-05-2022<br><b>End date:</b> 22-08-2022</p><span class="more">MORE DETAIL</span></article>
  <article class="program-card"><div class="program-photo" role="img" aria-label="Players in orange jerseys at a faceoff"></div><span class="day-tag">SUNDAY</span><div class="card-head"><span>Class Name Here</span><span class="price">$500.00</span></div><p class="card-text">Lorem ipsum dolor sit amet, consectetur adipiscing elit, sed do eiusmod tempor incididunt ut labore et dolore magna...</p><p class="card-dates"><b>Start date:</b> 22-05-2022<br><b>End date:</b> 22-08-2022</p><span class="more">MORE DETAIL</span></article>
  <article class="program-card"><div class="program-photo" role="img" aria-label="Faceoff with referee on the ice"></div><span class="day-tag">FRIDAY</span><div class="card-head"><span>Class Name Here</span><span class="price">$500.00</span></div><p class="card-text">Lorem ipsum dolor sit amet, consectetur adipiscing elit, sed do eiusmod tempor incididunt ut labore et dolore magna...</p><p class="card-dates"><b>Start date:</b> 22-05-2022<br><b>End date:</b> 22-08-2022</p><span class="more">MORE DETAIL</span></article>
  <article class="program-card"><div class="program-photo" role="img" aria-label="Young player skating on open ice"></div><span class="day-tag">MONDAY</span><div class="card-head"><span>Class Name Here</span><span class="price">$600.00</span></div><p class="card-text">Lorem ipsum dolor sit amet, consectetur adipiscing elit, sed do eiusmod tempor incididunt ut labore et dolore magna...</p><p class="card-dates"><b>Start date:</b> 22-05-2022<br><b>End date:</b> 22-08-2022</p><span class="more">MORE DETAIL</span></article>
  <article class="program-card"><div class="program-photo" role="img" aria-label="Players in orange jerseys at a faceoff"></div><span class="day-tag">SATURDAY</span><div class="card-head"><span>Class Name Here</span><span class="price">$300.00</span></div><p class="card-text">Lorem ipsum dolor sit amet, consectetur adipiscing elit, sed do eiusmod tempor incididunt ut labore et dolore magna...</p><p class="card-dates"><b>Start date:</b> 22-05-2022<br><b>End date:</b> 22-08-2022</p><span class="more">MORE DETAIL</span></article>
</main>

<footer class="site-footer">
  <div class="footer-contact">
    <h3>Contact Now</h3>
    <div class="contact-line">+112 345 6789 <svg viewBox="0 0 10 10"><path d="M2 1 L4 1 L4.5 3 L3.3 3.8 Q4.5 6 6.2 6.8 L7 5.6 L9 6 L9 8 Q5 9 2.5 6 Q1 4 2 1Z" fill="#fff"/></svg></div>
    <div class="contact-line">info@example.com <svg viewBox="0 0 10 10"><rect x="0.5" y="2" width="9" height="6.5" fill="#fff"/><path d="M0.5 2 L5 5.5 L9.5 2" stroke="var(--footer)" fill="none"/></svg></div>
    <div class="contact-line">253 Main Street, Lorem <svg viewBox="0 0 10 10"><path d="M5 0.5 A3.3 3.3 0 0 1 8.3 3.8 Q8.3 6 5 9.5 Q1.7 6 1.7 3.8 A3.3 3.3 0 0 1 5 0.5Z" fill="#fff"/><circle cx="5" cy="3.8" r="1.2" fill="var(--footer)"/></svg></div>
  </div>
  <div class="footer-badge">BRAVERIDGE<br>HOCKEY<br>DEVELOPMENT</div>
  <div class="footer-about">
    <h3>About US</h3>
    <p>Lorem ipsum dolor sit amet, consecte adipiscing elit, sed do eiusmod tempor incididunt ut labore sed do eiusmod incididunt ut labore....</p>
  </div>
  <div class="footer-social"><span></span><span></span><span></span><span></span></div>
</footer>
<div class="footer-bottom">2022 All rights reserved</div>

</body>
</html>
```